ROLL-UP DESIGN FOR SUPERMARKET DELIVERY

We need the graphic design of a roll-up with measurements 200 cm height x cm 85 width, for a supermarket delivery service.

The main logo "The Velarno" either color version or black version must be present very visible on the design.

the second logo attached 'CALVESINOSHOP' must also be present but smaller on the design.

the following text must be present on the design: CONSEGNA STESSO GIORNO.

Printing instruction attached must be respected.

Target Market(s)

HIGH END ITALIAN AND EUROPEAN SUPERMARKET CLIENTELE

Industry/Entity Type

FOOD DELIVERY

Requirements
Must have
• LOGOS ATTACHED
Nice to have
• PHOTOS OF SEA, SARDINIA, LUXURY DELIVERY, YACHTS

```html
<!DOCTYPE html>
<html lang="it">
<head>
<meta charset="utf-8">
<title>The Velarno – Roll-up Consegna Stesso Giorno</title>
<link rel="stylesheet" href="https://fonts.googleapis.com/css2?family=Poppins:wght@500;700&family=Bebas+Neue&display=swap">
<style>
  :root {
    --page-bg: #2b2b2b;
    --banner-bg: #f4f4f3;
    --ink: #161616;
    --orange: #e8842a;
    --sky-top: #e4ebf3;
    --sky-low: #cfdbe8;
    --hill: #4f6a45;
    --sea: #6f8e96;
    --rock: #3e4a4f;
  }
  * { margin: 0; padding: 0; box-sizing: border-box; }
  html, body {
    width: 1200px;
    height: 946px;
    overflow: hidden;
    background: var(--page-bg);
  }
  .rollup {
    position: absolute;
    left: 413px;
    top: 33px;
    width: 374px;
    height: 880px;
    background: var(--banner-bg);
    overflow: hidden;
  }
  .brand {
    position: absolute;
    top: 36px;
    left: 0;
    width: 100%;
    display: flex;
    justify-content: center;
    align-items: center;
    gap: 10px;
  }
  .brand-dot {
    width: 14px;
    height: 14px;
    border-radius: 50%;
    background: var(--ink);
    flex: none;
  }
  .brand-name {
    font-family: "Poppins", sans-serif;
    font-weight: 500;
    font-size: 24px;
    letter-spacing: 1px;
    color: var(--ink);
    line-height: 1;
  }
  .coast-photo {
    position: absolute;
    top: 104px;
    left: 0;
    width: 374px;
    height: 520px;
    display: block;
  }
  .headline {
    position: absolute;
    top: 641px;
    left: 0;
    width: 100%;
    text-align: center;
  }
  .headline-kicker {
    font-family: "Poppins", sans-serif;
    font-weight: 500;
    font-size: 13px;
    letter-spacing: 5px;
    color: var(--ink);
    padding-left: 5px;
  }
  .headline-main {
    font-family: "Bebas Neue", sans-serif;
    font-size: 108px;
    line-height: 0.9;
    letter-spacing: 12px;
    padding-left: 12px;
    color: var(--orange);
    margin-top: 4px;
  }
  .partner {
    position: absolute;
    top: 752px;
    left: 0;
    width: 100%;
    text-align: center;
    font-family: "Poppins", sans-serif;
    font-weight: 700;
    font-size: 16px;
    letter-spacing: 0.5px;
    color: var(--orange);
  }
</style>
</head>
<body>
  <main class="rollup">
    <header class="brand">
      <span class="brand-dot"></span>
      <span class="brand-name">The Velarno</span>
    </header>

    <svg class="coast-photo" viewBox="0 0 374 520" role="img" aria-label="Foto di una baia mediterranea con barche ormeggiate, scogli in primo piano e una collina verde a picco sul mare">
      <defs>
        <linearGradient id="coast-tones" x1="0" y1="0" x2="0" y2="1">
          <stop offset="0" stop-color="var(--sky-top)"/>
          <stop offset="0.35" stop-color="var(--sky-low)"/>
          <stop offset="0.6" stop-color="var(--hill)"/>
          <stop offset="0.75" stop-color="var(--sea)"/>
          <stop offset="1" stop-color="var(--rock)"/>
        </linearGradient>
      </defs>
      <path fill="url(#coast-tones)" d="M0,24 L10,22 18,27 28,20 40,23 52,18 66,21 80,15 96,17 112,14 128,18 142,13 158,16 176,11 196,13 214,9 232,12 250,6 268,9 286,4 304,10 322,7 340,12 356,9 374,12
        L374,440 L362,444 350,450 340,448 326,456 314,454 302,462 290,460 276,468 262,466 248,474 236,472 222,480 208,478 194,486 182,484 168,490 154,488 140,494 126,492 112,498 98,496 84,502 70,500 56,506 42,504 28,510 16,508 0,512 Z"/>
    </svg>

    <section class="headline">
      <div class="headline-kicker">CONSEGNA STESSO</div>
      <div class="headline-main">GIORNO</div>
    </section>

    <div class="partner">CALVESINOSHOP</div>
  </main>
</body>
</html>
```